Surface Protection company needs cards

We are a New Zealand company that will apply nanotechnology coatings on surfaces to prevent growth and spread of bacteria, viruses, mold etc with a sprayer. We deal with large corporates, airlines, hospitals and schools so we are after a new modern, simple and clean look that will have great visual impact.
We a company that is focused on prevention and protection.

Company name, Vela Shield

Subtext, Antimicrobial Surface Protection

Logo, VS

Target Market(s)

Hospitals, Transport agencies, Airlines, Corporate entities

Contact Information for Business Card

Company name, VelaShield
Logo, VS

Gareth Tolley
velashieldnz@postbox.example
+64219305562
www.velashield.example.nz

Requirements
Must have
• Simple clean look.
Nice to have
• We apply nano coatings so try and incorporate this into a theme somehow

```html
<!DOCTYPE html>
<html lang="en">
<head>
<meta charset="utf-8">
<title>Vela Shield – Business Card</title>
<link rel="stylesheet" href="https://fonts.googleapis.com/css2?family=Poppins:ital,wght@0,400;0,600;0,800;1,400&display=swap">
<style>
  :root {
    --brand-blue: #2a7fc9;
    --brand-green: #7cc242;
    --card-white: #ffffff;
    --card-dark: #161616;
    --text-light: #f2f2f2;
    --backdrop: #2b2b2b;
  }
  * { box-sizing: border-box; margin: 0; padding: 0; }
  html, body {
    width: 1200px; height: 900px; overflow: hidden;
    background: var(--backdrop);
    font-family: "Poppins", sans-serif;
  }
  .sheet {
    width: 1200px; height: 900px;
    display: flex; flex-direction: column;
    align-items: center; justify-content: center; gap: 50px;
  }
  .card {
    width: 630px; height: 360px; position: relative;
    border-radius: 4px; overflow: hidden;
    box-shadow: 0 10px 30px rgba(0,0,0,.45);
  }

  /* Front */
  .card--front {
    background: var(--card-white);
    display: flex; flex-direction: column; align-items: center; justify-content: center;
  }
  .brand-mark { display: flex; align-items: center; gap: 18px; }
  .brand-dot {
    width: 64px; height: 64px; border-radius: 50%;
    border: 6px solid var(--brand-blue);
  }
  .brand-name {
    color: var(--brand-blue); font-weight: 800; font-size: 52px;
    letter-spacing: 1px; text-transform: uppercase; line-height: 1;
  }
  .brand-tagline {
    margin-top: 12px; color: var(--brand-green); font-weight: 800;
    font-size: 17px; letter-spacing: 2px; text-transform: uppercase;
  }
  .brand-url {
    margin-top: 26px; color: var(--brand-blue); font-size: 17px; letter-spacing: .5px;
  }

  /* Back */
  .card--back { background: var(--card-dark); }
  .person { position: absolute; left: 40px; top: 44px; }
  .person__name {
    display: inline-block; background: var(--brand-blue); color: var(--card-white);
    font-weight: 600; font-size: 22px; padding: 3px 36px 3px 16px;
    border-radius: 20px;
  }
  .person__title {
    margin-top: 6px; color: var(--brand-green); font-style: italic; font-size: 14px;
  }
  .contacts {
    position: absolute; left: 40px; bottom: 54px; list-style: none;
    color: var(--text-light); font-size: 14px;
  }
  .contacts li { display: flex; align-items: center; gap: 10px; margin-top: 6px; }
  .contacts svg { width: 16px; height: 16px; flex: none; }
  .back-mark {
    position: absolute; right: 40px; top: 50%; transform: translateY(-50%);
    width: 250px; height: 250px; border-radius: 50%;
    border: 8px solid var(--brand-blue);
    display: flex; align-items: center; justify-content: center;
  }
  .back-mark__name {
    color: var(--brand-blue); font-weight: 800; font-size: 30px;
    text-transform: uppercase; text-align: center; line-height: 1.1;
  }
</style>
</head>
<body>
<main class="sheet">

  <section class="card card--front" aria-label="Card front">
    <div class="brand-mark">
      <span class="brand-dot"></span>
      <span class="brand-name">Vela Shield</span>
    </div>
    <p class="brand-tagline">Antimicrobial Surface Protection</p>
    <p class="brand-url">www.velashield.example.nz</p>
  </section>

  <section class="card card--back" aria-label="Card back">
    <div class="person">
      <p class="person__name">Gareth Tolley</p>
      <p class="person__title">CEO &amp; Executive Director</p>
    </div>

    <ul class="contacts">
      <li>
        <svg viewBox="0 0 16 16" aria-hidden="true"><path fill="#7cc242" d="M4 1l3 3-2 2c1 2 3 4 5 5l2-2 3 3-2 3C7 15 1 9 1 3z"/></svg>
        +64219305562
      </li>
      <li>
        <svg viewBox="0 0 16 16" aria-hidden="true"><rect x="1" y="3" width="14" height="10" fill="#7cc242"/><path d="M1 3l7 6 7-6" fill="none" stroke="#161616" stroke-width="1.4"/></svg>
        velashieldnz@postbox.example
      </li>
      <li>
        <svg viewBox="0 0 16 16" aria-hidden="true"><g fill="none" stroke="#7cc242" stroke-width="1.4"><circle cx="8" cy="8" r="6.5"/><ellipse cx="8" cy="8" rx="3" ry="6.5"/><path d="M1.5 8h13M2.5 5h11M2.5 11h11"/></g></svg>
        www.velashield.example.nz
      </li>
    </ul>

    <div class="back-mark">
      <span class="back-mark__name">Vela<br>Shield</span>
    </div>
  </section>

</main>
</body>
</html>
```